Kestrel Ridge Trophies & Awards Unique Business Card Design

Recently selected a new logo design and waiting to recieve print files. I've attached image for your review. We are a trophies and awards company that provides engraving on trophies, plaques, name plates, name tags, desk sets, medals, acrylics, and signage.

We are located in Monroe, Louisiana and provide this service with computerized & laser engraving equipment.

Target Market(s)

Corporate, Sport, Church, and Special Events

Industry/Entity Type

Business

Contact Information for Business Card

I'd like to see the following list on the card: Trophies, Plaques, Name Plates, Name Tags, Desk Sets, Medals, Certificates... this is accomplished with Computerized & Laser Engraving

Colors
0555a3
ec1f27
ffffff

Requirements
Must have
• I like either single or double sided. If a design can be created with a frosted card stock I'd consider single. Must be Red, White, and Blue. Dalton Wrenfield - Owner, 418 W 9th Ave, Monroe, La 71201 office 318-555-0186 fax 318-555-0142 email: kestrel@kestrelridgetrophiesawards.example, and website: www.kestrelridgetrophiesawards.example

```html
<!DOCTYPE html>
<html lang="en">
<head>
<meta charset="utf-8">
<title>Kestrel Ridge Trophies &amp; Awards – Business Card</title>
<link rel="stylesheet" href="https://fonts.googleapis.com/css2?family=Questrial&display=swap">
<style>
  :root {
    --blue: #0555a3;
    --navy: #1f3f7a;
    --red: #ec1f27;
    --deep-red: #a8141b;
    --white: #ffffff;
    --card: #f3f5f7;
    --stage: #dcdfe3;
  }
  * { box-sizing: border-box; margin: 0; padding: 0; }
  html, body { width: 1200px; height: 970px; overflow: hidden; }
  body {
    background: var(--stage);
    font-family: "Questrial", sans-serif;
    position: relative;
  }
  .card {
    position: absolute;
    left: 61px; top: 185px;
    width: 1078px; height: 600px;
    background: var(--card);
    overflow: hidden;
    box-shadow: 0 10px 30px rgba(0,0,0,0.12);
  }
  .brand {
    position: absolute;
    left: 43px; top: 58px;
    width: 600px;
    color: var(--navy);
    font-size: 50px;
    line-height: 1.05;
    border-bottom: 2px solid var(--blue);
    padding-bottom: 12px;
  }
  .trophy-art {
    position: absolute;
    right: 0; top: 0;
    width: 150px; height: 536px;
    background: linear-gradient(180deg, #b32028 0%, #b32028 12%, #1f6fc0 14%, #0555a3 70%, #6fa4d8 100%);
    opacity: 0.9;
  }
  .person { position: absolute; left: 43px; top: 275px; }
  .person-name { color: var(--deep-red); font-size: 29px; }
  .person-role {
    color: var(--navy); font-size: 23px;
    display: flex; align-items: center; gap: 8px; margin-top: 2px;
  }
  .person-role::after {
    content: ""; display: block; width: 385px; height: 2px;
    background: linear-gradient(90deg, var(--blue), rgba(5,85,163,0));
  }
  .contacts {
    position: absolute; left: 43px; top: 362px;
    list-style: none;
    color: var(--navy); font-size: 23px;
  }
  .contacts li { display: flex; align-items: center; gap: 9px; height: 31px; }
  .contacts li.address { margin-top: 7px; }
  .contacts svg { width: 16px; height: 16px; fill: var(--deep-red); flex: none; }
  .tagline {
    position: absolute; left: 560px; top: 362px; width: 340px;
    text-align: center; color: var(--blue); font-size: 23px; line-height: 1.35;
    white-space: nowrap;
  }
  .services {
    position: absolute; left: 0; bottom: 0;
    width: 100%; height: 64px;
    background: linear-gradient(90deg, var(--deep-red), var(--red) 50%, var(--deep-red));
    color: #f6e0e0;
    display: flex; align-items: center; justify-content: center;
    font-size: 23px; gap: 8px;
  }
  .services .star { font-size: 15px; color: #f3d7d7; }
</style>
</head>
<body>
  <main class="card">
    <h1 class="brand">Kestrel Ridge<br>Trophies &amp; Awards</h1>

    <div class="trophy-art" role="img" aria-label="Large red, white and blue trophy cup illustration with stars"></div>

    <section class="person">
      <p class="person-name">Dalton Wrenfield</p>
      <p class="person-role">Owner</p>
    </section>

    <ul class="contacts">
      <li><svg viewBox="0 0 16 16"><path d="M3 1l3 3-2 2c1 2 3 4 5 5l2-2 3 3-2 3C7 15 1 9 0 4z"/></svg>318-555-0186</li>
      <li><svg viewBox="0 0 16 16"><path d="M4 1h8v4H4zM1 6h14v6h-3v3H4v-3H1zM5 10v4h6v-4z"/></svg>318-555-0142</li>
      <li><svg viewBox="0 0 16 16"><path d="M1 3h14v10H1zM2 4l6 5 6-5v1L8 10 2 5z" fill-rule="evenodd"/></svg>kestrel@kestrelridgetrophiesawards.example</li>
      <li><svg viewBox="0 0 16 16"><path d="M8 1a7 7 0 100 14A7 7 0 008 1zm0 1.5c.8 1 1.4 2.6 1.5 4.5h-3C6.6 5.1 7.2 3.5 8 2.5zM2.6 7a5.5 5.5 0 013-4 9 9 0 00-.8 4zm0 2h2.2a9 9 0 00.8 4 5.5 5.5 0 01-3-4zm3.9 0h3c-.1 1.9-.7 3.5-1.5 4.5-.8-1-1.4-2.6-1.5-4.5zm4.7 0h2.2a5.5 5.5 0 01-3 4 9 9 0 00.8-4zm0-2a9 9 0 00-.8-4 5.5 5.5 0 013 4z"/></svg>www.kestrelridgetrophiesawards.example</li>
      <li class="address"><svg viewBox="0 0 16 16"><path d="M8 0a5 5 0 00-5 5c0 4 5 9 5 9s5-5 5-9a5 5 0 00-5-5zm0 3a2 2 0 110 4 2 2 0 010-4zM2 14h12v2H2z"/></svg>418 W 9th Ave, Monroe, La 71201</li>
    </ul>

    <p class="tagline">Accomplished with<br>Computerized &amp; Lase Engraving</p>

    <p class="services">
      <span class="star">★</span>Trophies <span class="star">★</span>Plaques <span class="star">★</span>Name Plates <span class="star">★</span>Name Tags <span class="star">★</span>Desk Sets <span class="star">★</span>Medals <span class="star">★</span>Certificates <span class="star">★</span>
    </p>
  </main>
</body>
</html>
```